Tevrix BIM business website

I have a logo design and business card concept is ongoing at this point, but i need a website design based on VDC or BIM ("Virtual Building and Construction" or "Building Information Modeling") that will stand out for the quality and concept that we provide. I am a consultant providing training and production work for Quorvel (Zembrick application <where most of the overview can be obtained>). We are providing BIM production and coordination services as well. I can fill in the meat but I need an open development website. Currently, just obtaining a domain so it can be included on a business card is the quickest objective, then developing the content and launching it.

Business

```html
<!DOCTYPE html>
<html lang="en">
<head>
<meta charset="utf-8">
<title>Tevrix BIM Consulting</title>
<link href="https://fonts.googleapis.com/css2?family=Lato:wght@400;700;900&display=swap" rel="stylesheet">
<style>
:root{
  --navy:#212a5c;
  --navy-deep:#1b234f;
  --orange:#f0a73a;
  --ink:#333a4a;
  --muted:#555b66;
  --grey-bg:#ececee;
  --light-bg:#f4f5f7;
  --white:#ffffff;
  --hero-a:#0b3f82;
  --hero-b:#1f66b3;
}
*{margin:0;padding:0;box-sizing:border-box}
html,body{width:1200px;height:3249px;overflow:hidden}
body{position:relative;font-family:'Lato',sans-serif;color:var(--ink);background:var(--white)}
.abs{position:absolute}

/* Header */
.site-header{left:0;top:0;width:1200px;height:139px;background:var(--navy)}
.brand{left:132px;top:20px;width:140px;text-align:center;color:var(--orange)}
.brand-mark{display:block;width:34px;height:34px;border-radius:50%;background:var(--orange);margin:0 auto 4px}
.brand-name{display:block;font-size:30px;font-weight:900;line-height:32px}
.brand-tag{display:block;font-size:10px;font-weight:700;letter-spacing:2px;color:var(--orange)}
.call-icon{left:704px;top:26px}
.call-label{left:760px;top:28px;font-size:11px;font-weight:700;color:var(--white);letter-spacing:.5px}
.call-number{left:760px;top:46px;font-size:22px;font-weight:700;color:var(--orange)}
.search{left:925px;top:26px;width:143px;height:37px;border:1px solid #3a4476;background:var(--navy-deep);display:flex;align-items:center;padding-left:12px;gap:10px;font-size:10px;font-weight:700;color:var(--white)}
.main-nav{left:0;top:93px;height:26px;width:1200px}
.main-nav a{position:absolute;top:0;height:26px;line-height:26px;font-size:11.5px;font-weight:700;color:var(--white);text-decoration:none;text-transform:uppercase}
.main-nav a.active{background:var(--orange);padding:0 15px}

/* Hero */
.hero{left:0;top:139px;width:1200px;height:541px;background:linear-gradient(135deg,#0a3270 0%,var(--hero-a) 35%,var(--hero-b) 70%,#2b78c2 100%)}
.hero-title{left:736px;top:512px;font-size:45px;font-weight:900;line-height:54px;color:var(--white);text-transform:uppercase}
.hero-dots{left:556px;top:592px;display:flex;gap:14px}
.hero-dots span{width:11px;height:11px;border-radius:50%;border:2px solid var(--white)}
.hero-dots span.on{background:var(--white)}

/* Welcome */
.welcome{left:0;top:680px;width:1200px;height:435px;background:linear-gradient(180deg,#f7f8fa,#eef0f3)}
.section-title{font-size:27px;font-weight:700;color:var(--navy);text-transform:uppercase}
.title-rule{height:2px;background:var(--navy)}
.welcome-title{left:132px;top:747px}
.welcome-rule{left:132px;top:786px;width:297px}
.welcome-text{left:132px;top:833px;width:468px;font-size:13.5px;line-height:22.5px;color:var(--muted);text-align:justify}
.btn{display:block;background:var(--navy);color:var(--white);font-size:12px;font-weight:700;text-transform:uppercase;text-align:center;line-height:39px;height:39px;text-decoration:none}
.welcome-btn{left:136px;top:990px;width:128px}
.welcome-photo{left:671px;top:752px;width:397px;height:279px;background:linear-gradient(135deg,#1c2238,#4a3f66 55%,#9b7fb8)}

/* Services */
.services{left:0;top:1115px;width:1200px;height:564px;background:var(--grey-bg)}
.services-title{left:0;width:1200px;top:1169px;text-align:center}
.services-rule{left:511px;top:1217px;width:178px}
.service{top:1284px;width:300px}
.service-icon{height:86px}
.service h3{margin-top:30px;font-size:15px;font-weight:700;color:#222;line-height:20px}
.service p{margin-top:12px;width:255px;font-size:13.5px;line-height:22.5px;color:var(--muted)}
.service .btn{margin-top:34px;width:128px}

/* Projects */
.projects-title{left:0;width:1200px;top:1747px;text-align:center}
.projects-rule{left:377px;top:1798px;width:446px}
.projects-intro{left:264px;top:1846px;width:672px;text-align:center;font-size:14.5px;line-height:29px;color:var(--muted)}
.tile{top:1952px;width:233px;height:320px}
.tile-caption{position:absolute;left:0;top:232px;display:flex;gap:13px;align-items:flex-start}
.tile-arrow{width:37px;height:41px;background:var(--orange);display:flex;align-items:center;justify-content:center}
.tile-caption p{width:165px;font-size:15px;font-weight:700;line-height:17px;color:var(--white)}

/* Videos */
.videos-title{left:0;width:1200px;top:2339px;text-align:center}
.videos-rule{left:522px;top:2389px;width:156px}
.video{top:2448px;width:455px;height:314px}
.play{position:absolute;left:194px;top:123px;width:66px;height:66px;border-radius:50%;background:rgba(220,160,70,.85);display:flex;align-items:center;justify-content:center}

/* Footer */
.site-footer{left:0;top:2851px;width:1200px;height:398px;background:var(--navy)}
.footer-heading{font-size:11px;font-weight:700;color:var(--white);text-transform:uppercase;letter-spacing:.3px}
.contact-col{left:370px;top:2908px;width:200px}
.contact-line{position:absolute;left:0;display:flex;gap:14px;font-size:11px;line-height:18px;color:#dfe2ee;white-space:nowrap}
.contact-line svg{flex:none;margin-top:3px}
.menu-col{left:607px;top:2908px}
.menu-col ul{list-style:none;margin-top:24px}
.menu-col li{font-size:11px;line-height:22px;color:#dfe2ee;text-transform:uppercase}
.news-col{left:782px;top:2908px;width:286px}
.news-input{position:absolute;left:0;top:47px;width:286px;height:47px;background:var(--white);display:flex;align-items:center;gap:12px;padding-left:18px;font-size:12px;color:#666}
.news-btn{position:absolute;left:162px;top:114px;width:124px;height:34px;background:var(--orange);color:var(--navy);font-size:13px;font-weight:700;text-transform:uppercase;text-align:center;line-height:34px}
.footer-rule{left:132px;top:3134px;width:936px;height:1px;background:#39427a}
.follow{left:134px;top:3179px;font-size:11px;font-weight:700;color:var(--white);text-transform:uppercase}
.social{top:3171px;width:30px;height:30px;border-radius:50%}
.copyright{right:132px;top:3180px;font-size:10.5px;color:#dfe2ee}
</style>
</head>
<body>

<header class="abs site-header">
  <div class="abs brand">
    <span class="brand-mark"></span>
    <span class="brand-name">Tevrix</span>
    <span class="brand-tag">BIM CONSULTING</span>
  </div>
  <svg class="abs call-icon" width="36" height="36" viewBox="0 0 36 36"><circle cx="18" cy="18" r="16" fill="none" stroke="#fff" stroke-width="1.5"/><path d="M13 11c1-1 2 0 3 2s0 2-1 3c1 2 2 3 4 4 1-1 2-2 3-1s3 2 2 3c-1 2-3 3-5 2-4-2-6-4-8-8-1-2 0-4 2-5z" fill="#fff"/></svg>
  <div class="abs call-label">CALL US NOW</div>
  <div class="abs call-number">888.888.8888</div>
  <div class="abs search">
    <svg width="11" height="11" viewBox="0 0 12 12"><circle cx="5" cy="5" r="3.8" fill="none" stroke="#fff" stroke-width="1.6"/><path d="M8 8l3 3" stroke="#fff" stroke-width="1.6"/></svg>
    SEARCH
  </div>
  <nav class="abs main-nav">
    <a class="active" style="left:496px">Home</a>
    <a style="left:596px">About Us</a>
    <a style="left:708px">Services</a>
    <a style="left:812px">Training</a>
    <a style="left:918px">Blog</a>
    <a style="left:996px">Contact Us</a>
  </nav>
</header>

<section class="abs hero" role="img" aria-label="Blue wireframe drawing of city skyscrapers"></section>
<h1 class="abs hero-title">Virtual Building &amp;<br>Construction</h1>
<div class="abs hero-dots"><span></span><span class="on"></span><span></span><span></span></div>

<section class="abs welcome"></section>
<h2 class="abs section-title welcome-title">Welcome to our site</h2>
<div class="abs title-rule welcome-rule"></div>
<p class="abs welcome-text">There are many variations of passages of Lorem Ipsum available, but the majority have suffered alteration in some form, by injected humour, or randomised words which don't look even slightly believable. If you are going to use a passage of Lorem Ipsum, you need to be sure there isn't anything embarrassing hidden in the middle of text.</p>
<a class="abs btn welcome-btn">Read More</a>
<div class="abs welcome-photo" role="img" aria-label="Business consultant touching a glowing 3D building model on a tablet"></div>

<section class="abs services"></section>
<h2 class="abs section-title services-title">Our Services</h2>
<div class="abs title-rule services-rule"></div>

<div class="abs service" style="left:132px">
  <svg class="service-icon" width="80" height="86" viewBox="0 0 80 86"><rect x="20" y="8" width="52" height="40" fill="none" stroke="#1b2240" stroke-width="4"/><path d="M30 38l10-10 8 6 14-16" fill="none" stroke="#1b2240" stroke-width="3"/><path d="M46 48v10M34 84l12-26 12 26" stroke="#1b2240" stroke-width="4" fill="none"/></svg>
  <h3>Training</h3>
  <p>There are many variations of passages of Lorem Ipsum available, but the majority have suffered more-or-less normal.</p>
  <a class="btn">Read More</a>
</div>
<div class="abs service" style="left:477px">
  <svg class="service-icon" width="80" height="86" viewBox="0 0 80 86"><rect x="2" y="14" width="56" height="64" rx="6" fill="#1b2240"/><rect x="6" y="22" width="28" height="16" rx="3" fill="#fff"/><text x="20" y="34" font-family="Lato,sans-serif" font-size="11" font-weight="700" fill="#1b2240" text-anchor="middle">CAD</text><path d="M48 2v14M42 10l6 7 6-7" stroke="#1b2240" stroke-width="4" fill="none"/></svg>
  <h3>Production</h3>
  <p>There are many variations of passages of Lorem Ipsum available, but the majority have suffered more-or-less normal.</p>
  <a class="btn">Read More</a>
</div>
<div class="abs service" style="left:825px">
  <svg class="service-icon" width="80" height="86" viewBox="0 0 80 86"><rect x="8" y="10" width="36" height="68" fill="none" stroke="#1b2240" stroke-width="4"/><rect x="44" y="34" width="22" height="44" fill="none" stroke="#1b2240" stroke-width="4"/><g fill="#1b2240"><rect x="15" y="18" width="8" height="8"/><rect x="29" y="18" width="8" height="8"/><rect x="15" y="32" width="8" height="8"/><rect x="29" y="32" width="8" height="8"/><rect x="15" y="46" width="8" height="8"/><rect x="29" y="46" width="8" height="8"/><rect x="50" y="42" width="10" height="6"/><rect x="50" y="54" width="10" height="6"/><rect x="22" y="62" width="10" height="16"/></g><path d="M2 80h72" stroke="#1b2240" stroke-width="4"/></svg>
  <h3>Construction</h3>
  <p>There are many variations of passages of Lorem Ipsum available, but the majority have suffered more-or-less normal.</p>
  <a class="btn">Read More</a>
</div>

<h2 class="abs section-title projects-title">Virtual Construction Projects</h2>
<div class="abs title-rule projects-rule"></div>
<p class="abs projects-intro">There are many variations of passages of Lorem Ipsum available, but the majority have suffered alteration in some form, by injected humour, or randomised words.</p>

<div class="abs tile" style="left:0;background:linear-gradient(160deg,#0a2a3a,#0f5a6e 60%,#12708a)" role="img" aria-label="Teal glass skyscrapers at night">
  <div class="tile-caption"><span class="tile-arrow"><svg width="10" height="14" viewBox="0 0 10 14"><path d="M2 2l5 5-5 5" stroke="#fff" stroke-width="2.5" fill="none"/></svg></span><p>Lorem Ipsum is simply dummy text of the printing</p></div>
</div>
<div class="abs tile" style="left:240px;background:linear-gradient(170deg,#02060f,#0c3c78 55%,#2a8ee0)" role="img" aria-label="Glowing blue 3D city model">
  <div class="tile-caption"><span class="tile-arrow"><svg width="10" height="14" viewBox="0 0 10 14"><path d="M2 2l5 5-5 5" stroke="#fff" stroke-width="2.5" fill="none"/></svg></span><p>Lorem Ipsum is simply dummy text of the printing</p></div>
</div>
<div class="abs tile" style="left:483px;background:linear-gradient(160deg,#d9a24a,#c8923d 60%,#b8843a)" role="img" aria-label="Amber tinted office towers">
  <div class="tile-caption"><span class="tile-arrow" style="background:#fff"><svg width="10" height="14" viewBox="0 0 10 14"><path d="M2 2l5 5-5 5" stroke="#c8923d" stroke-width="2.5" fill="none"/></svg></span><p>Lorem Ipsum is simply dummy text of the printing</p></div>
</div>
<div class="abs tile" style="left:726px;background:linear-gradient(160deg,#2b5ea8,#3a78c4 55%,#5a96d6)" role="img" aria-label="Blue rendered apartment facade">
  <div class="tile-caption"><span class="tile-arrow"><svg width="10" height="14" viewBox="0 0 10 14"><path d="M2 2l5 5-5 5" stroke="#fff" stroke-width="2.5" fill="none"/></svg></span><p>Lorem Ipsum is simply dummy text of the printing</p></div>
</div>
<div class="abs tile" style="left:968px;background:linear-gradient(160deg,#1d5aa8,#2f7acb 55%,#5aa0e0)" role="img" aria-label="Blue wireframe building drawing">
  <div class="tile-caption"><span class="tile-arrow"><svg width="10" height="14" viewBox="0 0 10 14"><path d="M2 2l5 5-5 5" stroke="#fff" stroke-width="2.5" fill="none"/></svg></span><p>Lorem Ipsum is simply dummy text of the printing</p></div>
</div>

<h2 class="abs section-title videos-title">Our Videos</h2>
<div class="abs title-rule videos-rule"></div>
<div class="abs video" style="left:132px;background:linear-gradient(160deg,#e6eef2,#9cc0cc 50%,#4a8496)" role="img" aria-label="Video still of a glass tower seen from below">
  <span class="play"><svg width="22" height="26" viewBox="0 0 22 26"><path d="M2 2l18 11L2 24z" fill="#fff"/></svg></span>
</div>
<div class="abs video" style="left:613px;background:linear-gradient(160deg,#1f6fd0,#3b8ae0 55%,#5ea2ea)" role="img" aria-label="Video still of a wireframe apartment block">
  <span class="play"><svg width="22" height="26" viewBox="0 0 22 26"><path d="M2 2l18 11L2 24z" fill="#fff"/></svg></span>
</div>

<footer class="abs site-footer"></footer>
<div class="abs brand" style="left:122px;top:2900px">
  <span class="brand-mark"></span>
  <span class="brand-name">Tevrix</span>
  <span class="brand-tag">BIM CONSULTING</span>
</div>

<div class="abs contact-col">
  <div class="footer-heading">Contact Us</div>
  <div class="contact-line" style="top:44px"><svg width="10" height="13" viewBox="0 0 10 13"><path d="M5 0a5 5 0 0 1 5 5c0 3-5 8-5 8S0 8 0 5a5 5 0 0 1 5-5z" fill="#fff"/><circle cx="5" cy="5" r="2" fill="#212a5c"/></svg><span>1420 Alder Street<br>Springfield, OH 45502</span></div>
  <div class="contact-line" style="top:92px"><svg width="11" height="11" viewBox="0 0 11 11"><path d="M2 0c1 0 2 2 2 3S3 4 3 4c1 2 2 3 4 4 0 0 1-1 1-1s2 1 3 2c0 1-1 2-2 2C5 11 0 6 0 2 0 1 1 0 2 0z" fill="#fff"/></svg><span>888.888.8888</span></div>
  <div class="contact-line" style="top:130px"><svg width="12" height="9" viewBox="0 0 12 9"><rect width="12" height="9" fill="#fff"/><path d="M0 0l6 5 6-5" stroke="#212a5c" stroke-width="1.2" fill="none"/></svg><span>info@tevrix.com</span></div>
</div>

<div class="abs menu-col">
  <div class="footer-heading">Menu</div>
  <ul><li>Home</li><li>About Us</li><li>Services</li><li>Training</li><li>Blog</li><li>Contact Us</li></ul>
</div>

<div class="abs news-col">
  <div class="footer-heading">Newsletter Signup</div>
  <div class="news-input"><svg width="13" height="10" viewBox="0 0 13 10"><rect x=".6" y=".6" width="11.8" height="8.8" fill="none" stroke="#f0a73a" stroke-width="1.2"/><path d="M.6.6l5.9 5 5.9-5" stroke="#f0a73a" stroke-width="1.2" fill="none"/></svg>E mail id</div>
  <div class="news-btn">Signup</div>
</div>

<div class="abs footer-rule"></div>
<div class="abs follow">Follow Us</div>
<span class="abs social" style="left:219px;background:#3b5ba8"></span>
<span class="abs social" style="left:256px;background:#1da1e2"></span>
<span class="abs social" style="left:295px;background:#e05a3e"></span>
<div class="abs copyright">Copyrights @ 2017 All Rights Reserved</div>

</body>
</html>
```